Tradewell Banner Design for B2B Consulting Firm

Take the already developed logo (attached) and incorporate it into a creative banner design for placement on Tradewell (the social media platform targeting business users). The banner will be used on the firm's company profile page on Tradewell (not yet created).

```html
<!DOCTYPE html>
<html lang="en">
<head>
<meta charset="utf-8">
<title>Hartfield Growth – Tradewell Banner</title>
<link rel="stylesheet" href="https://fonts.googleapis.com/css2?family=Oswald:wght@600&family=Open+Sans:wght@400;600&display=swap">
<style>
  :root {
    --stage: #e4e4e4;
    --paper: #ffffff;
    --forest: #45654b;
    --ink-light: #ffffff;
    --photo-a: #3c5f86;
    --photo-b: #8fa9bd;
    --photo-c: #c9d6dc;
  }
  html, body {
    margin: 0;
    padding: 0;
    width: 1200px;
    height: 364px;
    overflow: hidden;
    background: var(--stage);
  }
  .banner {
    position: absolute;
    left: 57px;
    top: 90px;
    width: 1086px;
    height: 184px;
    background: var(--paper);
    overflow: hidden;
  }
  .banner__art {
    position: absolute;
    inset: 0;
  }
  .brand {
    position: absolute;
    left: 26px;
    top: 74px;
    display: flex;
    align-items: center;
    gap: 10px;
    font-family: "Oswald", sans-serif;
    font-weight: 600;
    font-size: 25px;
    color: var(--forest);
    letter-spacing: 0.2px;
    line-height: 1;
  }
  .brand__square {
    width: 22px;
    height: 22px;
    background: var(--forest);
  }
  .headline {
    position: absolute;
    left: 305px;
    top: 35px;
    margin: 0;
    font-family: "Oswald", sans-serif;
    font-weight: 600;
    font-size: 33px;
    line-height: 38px;
    color: var(--ink-light);
    white-space: pre;
  }
  .contact {
    position: absolute;
    left: 305px;
    top: 125px;
    display: flex;
    gap: 16px;
    font-family: "Open Sans", sans-serif;
    font-size: 10.5px;
    color: var(--ink-light);
  }
  .contact__item {
    display: flex;
    align-items: center;
    gap: 6px;
  }
  .contact__icon {
    width: 9px;
    height: 9px;
    fill: var(--ink-light);
  }
  .photo {
    position: absolute;
    left: 684px;
    top: 0;
    width: 402px;
    height: 184px;
    background: linear-gradient(100deg, var(--photo-a) 0%, var(--photo-b) 45%, var(--photo-c) 75%, var(--photo-b) 100%);
  }
  .frame-lines {
    position: absolute;
    inset: 0;
    pointer-events: none;
  }
</style>
</head>
<body>
  <div class="banner">
    <svg class="banner__art" width="1086" height="184" viewBox="0 0 1086 184" aria-hidden="true">
      <polygon points="277,26 684,26 684,159 223,159" fill="var(--forest)"/>
    </svg>

    <div class="brand">
      <span class="brand__square"></span>
      <span>Hartfield Growth</span>
    </div>

    <h1 class="headline">Fractional  Marketing
Services to B2B clients</h1>

    <div class="contact">
      <span class="contact__item">
        <svg class="contact__icon" viewBox="0 0 24 24"><path d="M6.6 10.8a15.1 15.1 0 0 0 6.6 6.6l2.2-2.2a1 1 0 0 1 1-.25 11.4 11.4 0 0 0 3.6.57 1 1 0 0 1 1 1V20a1 1 0 0 1-1 1A17 17 0 0 1 3 4a1 1 0 0 1 1-1h3.5a1 1 0 0 1 1 1c0 1.25.2 2.45.57 3.57a1 1 0 0 1-.25 1z"/></svg>
        +49 170 400 28 19
      </span>
      <span class="contact__item">
        <svg class="contact__icon" viewBox="0 0 24 24"><path d="M2 5h20v14H2z M2 5l10 8 10-8" fill="none" stroke="#fff" stroke-width="2.5"/></svg>
        hello@hartfieldgrowth.com
      </span>
    </div>

    <div class="photo" role="img" aria-label="Photo of a diverse team of colleagues smiling and discussing work around a table with a laptop in a bright office"></div>

    <svg class="frame-lines" width="1086" height="184" viewBox="0 0 1086 184" aria-hidden="true">
      <g fill="none" stroke="var(--ink-light)" stroke-width="2">
        <polyline points="651,26 651,61 716,61 716,0"/>
        <polyline points="651,159 651,100 716,100 716,184"/>
      </g>
    </svg>
  </div>
</body>
</html>
```